Stationery Design Project

We need a stationery design to change our look to a more corporate design. My company has been established since 1989 and over that time has changed from your average sign company to doing more Corporate re branding projects and have some multi National clients.
Our website is currently being redesigned so we need a new logo and business cards etc. to compliment it.
I have 2 graphic designers employed but i want on outsiders opinion and a totally independant view point.
Updates
Hi Designers
We are predominantely a sign manufacturing company that manufacturers every type of sign you can imagine. However the majoprity of our work is digital graphics. Our claim to faim is that we wrap the Harbourtown Skytrams and Cityglides which everyone seems to know in Sydney.We also do all sorts of Large format digital printing, vehicle wraps,vinyl signage,LED & Neon Illuminated signage,CNC Routing all materials,Laser cutting and Engraving, Architectural signage, Cut Out letters and Screenprinting.
Aswell as this we totally re-brand companies with internal wall graphics reception signage way finding signage and the like.We are a medium size company that has been trading since 1989 and has some very large reputable clients.
Our Company name is Brackwell Pty Ltd but like to have Signage and Graphics in our stationery.
Our details are as follows T: 9381 5027 F: 9381 5093 Unit 4, 22 Tallowood Lane.Kenbury Flats. NSW 2163 email mail@brackwellsigns.example our current website is being re-designed www.brackwellsigns.example
The design and colour scheme i would like is quite simple with a corporate feel and blue, grey & magenta are colours that seem to suit but am open to most suggestions just looking for clean lines.
Hopefully this is enough information if you require any more please ask.
Regards Dennis Albrook
Reason: I did not supply much information at first
Reason: I have extended it due to Christmas holidays
We are looking to simplify our LOGO not too concerned yet about layout of stationery items that we can easily work on later. I want to get a new logo that we can work with before we return to work on the 16th January so please concentrate on just the logo for now.
We would like to have Signs & Graphics somewhere in the name even though our registered name is Brackwell Pty Ltd. Brackwell is one word, i want it to be quite a bold font with no seriffs.The bright blue and grey colours are favourites so far with maybe a little magenta added later. Would like to have a Logo that is totally seperate and then the Brackwell P/L Signs & graphics as a secondary item just to let people know what Brackwell do as the name obviously does not say what we are about.
Also we need to consider how we can put logo on T-shirts work shirts and company vehicles.
We do not need CD cover or envelopes but letterheads and business cards.
Reason: I want everyone to concentrate on a logo we return to work on the 16th of January so would like to have at least a logo approved by then
Reason: We are close to making a decision and just need a few more days for a couple of designers to submit extra things we have asked of them.
Business

```html
<!DOCTYPE html>
<html lang="en">
<head>
<meta charset="utf-8">
<title>Brackwell Business Card</title>
<link rel="stylesheet" href="https://fonts.googleapis.com/css2?family=Noto+Sans:ital,wght@0,300;0,400;0,700;1,400&display=swap">
<style>
  :root {
    --page: #ffffff;
    --card: #0f4365;
    --wave-1: #072a45;
    --wave-2: #0a3452;
    --wave-3: #0c3b5b;
    --white: #ffffff;
    --soft-text: #d7e4ee;
    --tagline: #a9c6dc;
    --web-yellow: #d8b31f;
    --divider: #c9d9e6;
  }
  html, body {
    margin: 0;
    width: 1200px;
    height: 900px;
    overflow: hidden;
    background: var(--page);
    font-family: "Noto Sans", sans-serif;
  }
  .business-card {
    position: absolute;
    left: 156px;
    top: 246px;
    width: 904px;
    height: 444px;
    background: var(--card);
    overflow: hidden;
    color: var(--soft-text);
  }
  .card-waves {
    position: absolute;
    inset: 0;
  }
  .wordmark {
    position: absolute;
    left: 0;
    width: 468px;
    top: 212px;
    margin: 0;
    text-align: center;
    font-size: 74px;
    font-weight: 700;
    line-height: 1;
    color: var(--white);
    letter-spacing: -1px;
  }
  .tagline {
    position: absolute;
    left: 0;
    width: 468px;
    top: 302px;
    text-align: center;
    font-size: 18px;
    font-weight: 400;
    letter-spacing: 0.5px;
    color: var(--tagline);
  }
  .website {
    position: absolute;
    left: 0;
    width: 468px;
    top: 402px;
    text-align: center;
    font-size: 20px;
    color: var(--web-yellow);
    letter-spacing: 0.5px;
  }
  .divider {
    position: absolute;
    left: 474px;
    top: 110px;
    width: 2px;
    height: 222px;
    background: var(--divider);
  }
  .contact {
    position: absolute;
    left: 512px;
    top: 140px;
  }
  .person-name {
    margin: 0;
    font-size: 24px;
    font-style: italic;
    font-weight: 400;
    color: var(--white);
  }
  .person-role {
    margin: 0 0 0 74px;
    font-size: 10px;
    color: var(--soft-text);
    line-height: 1;
  }
  .email {
    margin: 26px 0 0;
    font-size: 20px;
    font-weight: 300;
    letter-spacing: 0.5px;
  }
  .phones {
    margin: 30px 0 0;
    font-size: 20px;
    font-weight: 300;
    line-height: 30px;
    letter-spacing: 0.5px;
  }
  .address {
    position: absolute;
    left: 512px;
    top: 404px;
    font-size: 15px;
    font-weight: 300;
    letter-spacing: 0.3px;
    font-style: normal;
  }
</style>
</head>
<body>
  <div class="business-card">
    <svg class="card-waves" viewBox="0 0 904 444" width="904" height="444" aria-hidden="true">
      <path d="M0 0 H904 V70 C620 60 300 90 0 190 Z" fill="var(--wave-3)"/>
      <path d="M0 0 H904 V40 C600 30 280 60 0 150 Z" fill="var(--wave-2)"/>
      <path d="M0 0 H904 V18 C580 10 260 30 0 100 Z" fill="var(--wave-1)"/>
    </svg>

    <h1 class="wordmark">Brackwell</h1>
    <div class="tagline">SIGN TECHNOLOGY</div>
    <div class="website">www.brackwellsigns.example</div>

    <div class="divider"></div>

    <div class="contact">
      <p class="person-name">Aaron Pelley</p>
      <p class="person-role">Manager</p>
      <p class="email">mail@brackwellsigns.example</p>
      <p class="phones">Tel.  9381 5027<br>Fax.  9381 5093</p>
    </div>

    <address class="address">Unit 4, 22 Tallowood Lane.Kenbury Flats. NSW 2163</address>
  </div>
</body>
</html>
```